Electric mountain bike tours nz

We are an Electric Mountain bike tour company in New Zealand. We will be offering bike rental and guided tours around the Nelson region in New Zealand. I want our website to represent both Mountain biking and New Zealand with the colours layout and features. We want tabs for the following:
-1 about us
-2 what we offer
-3 bookings/contact
Under the about us tab will be who we are as a a company. I want the ability to add videos to each of these tabs as we move foward with videos of the tracks we will be riding. I want the website to be editable so I can add and remove videos/photos myself. Also "our bikes" will be under this tab.
Under the what we offer tab will be
-1 bike rental and pricing
-2 guided tours and pricing
-3 recommended package deals.
I want to able to put the tracks under the guided tours tab and select beginner/ intermediate/advanced and have the tracks in each of the following to match the rider level. Also to be able to have a small video of the track would be great in this section.
Bookings and contact tab
(Further information for this tab to be updated soon)
- Silver ferns, kiwi, mountains

```html
<!DOCTYPE html>
<html lang="en">
<head>
<meta charset="utf-8">
<title>Ridgeline – Electric Mountain Bike Tours New Zealand</title>
<link rel="stylesheet" href="https://fonts.googleapis.com/css2?family=Montserrat:wght@400;500;600;700&display=swap">
<style>
:root{
  --green:#3cb521;
  --ink:#222528;
  --muted:#6b6f73;
  --line:#d9dcdf;
  --white:#ffffff;
  --paper:#f2f3f5;
  --night:#0e1820;
  --frame:#15304f;
}
*{box-sizing:border-box;margin:0;padding:0}
html,body{width:1200px;height:3125px;overflow:hidden}
body{position:relative;font-family:"Montserrat",Arial,sans-serif;color:var(--ink);background:var(--white)}
.abs{position:absolute}
.photo{position:absolute}
.btn{position:absolute;display:flex;align-items:center;justify-content:center;font-size:12px;font-weight:600;letter-spacing:1px;color:var(--green);border:2px solid var(--green);background:var(--white);text-transform:uppercase}
.green{color:var(--green)}

/* hero */
.hero-photo{left:0;top:0;width:1200px;height:638px;background:linear-gradient(180deg,#8a96a8 0%,#b6bcc2 22%,#7f9a52 45%,#6f8d3b 70%,#8e8a5d 100%)}
.social{left:112px;top:38px;display:flex;gap:9px}
.social span{width:24px;height:24px;border-radius:50%;background:var(--white)}
.brand{left:540px;top:8px;display:flex;align-items:center;justify-content:center;width:120px;height:96px;background:var(--white);font-size:17px;font-weight:700;letter-spacing:1px;color:var(--ink)}
.nav{left:735px;top:44px;display:flex;gap:30px;font-size:12px;font-weight:500;letter-spacing:1px;color:var(--white)}
.hero-box{left:557px;top:198px;width:531px;height:230px;background:rgba(40,40,40,.6);text-align:center;color:var(--white)}
.hero-box .kicker{margin-top:30px;font-size:20px;font-weight:600;line-height:24px;letter-spacing:.5px}
.hero-box h1{font-size:48px;font-weight:600;letter-spacing:1.5px;margin-top:6px}
.hero-box .btn{left:209px;top:157px;width:112px;height:42px;border:none}
.arrows{left:567px;top:576px;display:flex;gap:8px}
.arrows span{width:28px;height:28px;border-radius:50%;background:var(--white);display:flex;align-items:center;justify-content:center}

/* who we are */
.who{left:0;top:638px;width:1200px;height:184px;background:linear-gradient(180deg,#fafafa,#eceef0)}
.who h2{position:absolute;top:66px;width:100%;text-align:center;font-size:32px;font-weight:500;letter-spacing:1px}
.who p{position:absolute;top:118px;width:100%;text-align:center;font-size:11px;line-height:19px;color:var(--muted)}
.who a{color:var(--green);font-weight:600;text-decoration:underline}

.video-title{position:absolute;width:100%;text-align:center;font-size:26px;font-weight:500;color:var(--white);letter-spacing:.5px}
.play{position:absolute;width:44px;height:44px}

.tracks-a{left:0;top:822px;width:682px;height:520px;background:linear-gradient(135deg,#2f3a22,#4b5a32 45%,#3a3324 100%)}
.bikes{left:690px;top:822px;width:510px;height:520px;background:var(--white);border:1px solid var(--line)}
.bikes h3{position:absolute;left:26px;top:42px;font-size:21px;font-weight:600;letter-spacing:.5px}
.bikes .lead{position:absolute;left:26px;top:74px;width:360px;font-size:11px;line-height:19px;color:var(--muted)}
.bike-photo{left:45px;top:135px;width:330px;height:200px;background:radial-gradient(ellipse at center,#9a9a9a 0%,#d8d8d8 55%,#ffffff 72%)}
.bikes .name{position:absolute;left:0;width:480px;top:360px;text-align:center;font-size:13px;font-weight:600;letter-spacing:1px}
.bikes .desc{position:absolute;left:0;width:480px;top:378px;text-align:center;font-size:10px;line-height:15px;color:var(--muted)}
.bikes .btn{left:150px;top:432px;width:115px;height:43px}

/* what we offer */
.offer-h{left:0;top:1405px;width:1200px;text-align:center;font-size:32px;font-weight:500;letter-spacing:1px}
.offer-band{left:0;top:1470px;width:1200px;height:525px;background:linear-gradient(180deg,#e7ecf0 0%,#90a6ba 40%,#3f5f3e 80%,#23456f 100%)}
.card{position:absolute;background:var(--white);box-shadow:0 2px 8px rgba(0,0,0,.18)}
.tours{left:113px;top:1468px;width:445px;height:560px}
.tours .num{position:absolute;left:16px;top:10px;font-size:78px;font-weight:700;color:#eef0f1}
.tours h3{position:absolute;left:82px;top:92px;font-size:22px;font-weight:600;letter-spacing:.5px}
.tours .pager{position:absolute;right:14px;top:52px;font-size:18px;color:#bbb}
.tours .levels{position:absolute;left:0;width:445px;top:140px;text-align:center;font-size:11px;font-weight:500;color:var(--muted)}
.tours .tour-photo{left:17px;top:180px;width:411px;height:262px;border:1px solid var(--line);background:radial-gradient(ellipse at center,#7d7d7d 0%,#cfcfcf 55%,#ffffff 75%)}
.tours .price{position:absolute;left:167px;top:420px;width:112px;height:40px;border-radius:20px;background:var(--green);color:var(--white);font-size:16px;font-weight:600;display:flex;align-items:center;justify-content:center}
.tours .caption{position:absolute;left:0;width:445px;top:474px;text-align:center;font-size:15px;font-weight:600}
.dots{position:absolute;left:204px;top:526px;display:flex;gap:5px}
.dots span{width:8px;height:8px;border-radius:50%;background:#ccc}
.dots span:first-child{background:var(--green)}
.tracks-b{left:568px;top:1468px;width:520px;height:560px}
.tracks-b .video{left:0;top:0;width:520px;height:397px;background:linear-gradient(160deg,#3d4a3a,#5b5a42 50%,#7a6a4a 100%)}
.tracks-b p{position:absolute;left:10px;width:500px;top:425px;text-align:center;font-size:17px;line-height:25px;color:#555}
.tracks-b .btn{left:190px;top:492px;width:114px;height:43px}

/* feature */
.feature-frame{left:385px;top:2200px;width:815px;height:445px;background:var(--frame)}
.feature-panel{left:391px;top:2207px;width:809px;height:432px;background:linear-gradient(180deg,#f7f8f9,#eef0f2)}
.feature-art{left:1010px;top:2420px;width:165px;height:180px;background:radial-gradient(ellipse at center,#d0d4d8 0%,rgba(238,240,242,0) 70%)}
.feature-bike{left:0;top:2095px;width:510px;height:400px;background:radial-gradient(ellipse at 50% 55%,#2a2d30 0%,#5a5d60 35%,rgba(255,255,255,0) 70%)}
.feature-text{left:690px;top:2296px;width:410px;text-align:center}
.feature-text h3{font-size:22px;font-weight:500;line-height:29px;letter-spacing:.5px}
.feature-text h3 b{font-weight:600}
.feature-text p{margin-top:18px;font-size:11px;line-height:20px;color:#666;text-align:justify}
.feature-btn{left:835px;top:2502px;width:113px;height:43px}

/* footer */
.footer{left:0;top:2720px;width:1200px;height:405px;background:linear-gradient(180deg,#3a4a55 0%,#1a2733 30%,var(--night) 70%,#081016 100%);color:var(--white)}
.footer h4{position:absolute;top:50px;font-size:14px;font-weight:600;letter-spacing:1px}
.footer .about{position:absolute;left:113px;top:93px;width:222px;font-size:10px;line-height:19px}
.footer ul{position:absolute;left:428px;top:87px;list-style:none;font-size:10px;font-weight:500;line-height:33px;letter-spacing:.3px}
.contact{position:absolute;left:698px;top:90px;font-size:10px;line-height:16px}
.contact div{display:flex;gap:10px;margin-bottom:16px}
.contact svg{flex:none}
.footer .social{left:915px;top:88px;gap:10px}
.footer .social span{width:32px;height:32px}
.footer hr{position:absolute;left:113px;top:230px;width:975px;border:none;border-top:1px solid rgba(255,255,255,.35)}
.footer-brand{left:545px;top:265px;width:110px;height:60px;display:flex;align-items:center;justify-content:center;font-size:15px;font-weight:700;letter-spacing:1px;color:var(--white)}
.copy{position:absolute;top:352px;width:100%;text-align:center;font-size:10px}
</style>
</head>
<body>

<!-- Hero -->
<div class="photo hero-photo" role="img" aria-label="Rider on an electric mountain bike crossing a grassy alpine slope below rocky peaks"></div>
<div class="abs social" aria-label="Social links"><span></span><span></span><span></span><span></span></div>
<div class="abs brand">RIDGELINE</div>
<nav class="abs nav"><span>ABOUT</span><span>WHAT WE OFFER</span><span>BOOKING</span><span>CONTACT</span></nav>
<section class="abs hero-box">
  <p class="kicker">WE ARE AN ELECTRIC MOUNTAIN BIKE<br>TOUR COMPANY</p>
  <h1>NEW ZEALAND</h1>
  <span class="btn">Read more</span>
</section>
<div class="abs arrows">
  <span><svg width="12" height="12" viewBox="0 0 12 12"><path d="M8 1 3 6l5 5" fill="none" stroke="#333" stroke-width="2"/></svg></span>
  <span><svg width="12" height="12" viewBox="0 0 12 12"><path d="m4 1 5 5-5 5" fill="none" stroke="#333" stroke-width="2"/></svg></span>
</div>

<!-- Who we are -->
<section class="abs who">
  <h2>WHO WE ARE</h2>
  <p>Lorem ipsum dolor sit amet, consectetur adipiscing elit.<br>Donec quis lacus convallis, elementum turpis sed...<a>READ MORE</a></p>
</section>

<div class="photo tracks-a" role="img" aria-label="Forest trail with a trail sign and a mountain bike among tall trees">
  <div class="video-title" style="top:208px">WATCH THE TRACKS</div>
  <svg class="play" style="left:319px;top:254px" viewBox="0 0 44 44"><circle cx="22" cy="22" r="22" fill="#fff"/><path d="M17 13v18l14-9z" fill="#222"/></svg>
</div>

<section class="abs bikes">
  <h3>OUR BIKES</h3>
  <p class="lead">Lorem ipsum dolor sit amet, consectetuer adipiscing elit. Aenean commodo ligula eget dolor.</p>
  <div class="photo bike-photo" role="img" aria-label="Grey full-suspension electric mountain bike, side view"></div>
  <p class="name green">SED CONSEQUAT</p>
  <p class="desc">Aenean massa. Cum sociis natoque penatibus et<br>magnis dis parturient montes, nascetur.</p>
  <span class="btn">View all</span>
</section>

<!-- What we offer -->
<h2 class="abs offer-h">WHAT WE OFFER</h2>
<div class="photo offer-band" role="img" aria-label="Mountain valley landscape with blue ridges"></div>

<section class="card tours">
  <span class="num">02</span>
  <span class="pager">‹ <span class="green">›</span></span>
  <h3>GUIDED TOURS AND PRICING</h3>
  <p class="levels"><span class="green">BEGINNER</span> / &nbsp;INTERMEDIATE / &nbsp;ADVANCED</p>
  <div class="photo tour-photo" role="img" aria-label="Black electric mountain bike, side view"></div>
  <span class="price">$100.00</span>
  <p class="caption">Lorem Ipsum Dolor</p>
  <div class="dots"><span></span><span></span><span></span></div>
</section>

<section class="card tracks-b">
  <div class="photo video" role="img" aria-label="Orange mountain bike beside a road sign on a hilltop track">
    <div class="video-title" style="top:148px">WATCH THE TRACKS</div>
    <svg class="play" style="left:238px;top:194px" viewBox="0 0 44 44"><circle cx="22" cy="22" r="22" fill="#fff"/><path d="M17 13v18l14-9z" fill="#222"/></svg>
  </div>
  <p>Lorem ipsum dolor sit amet, consectetuer adipiscing elit. Aenean commodo ligula eget dolor aenean massa.</p>
  <span class="btn">View all</span>
</section>

<!-- Feature -->
<div class="abs feature-frame"></div>
<div class="abs feature-panel"></div>
<div class="photo feature-art" role="img" aria-label="Faint rider silhouette on a hill"></div>
<div class="photo feature-bike" role="img" aria-label="Black electric mountain bike, side view"></div>
<section class="abs feature-text">
  <h3>LOREM IPSUM DOLOR SIT AMET,<br><b>CONSECTETUER ADIPISCING ELIT.</b></h3>
  <p>In enim justo, rhoncus ut, imperdiet a, venenatis vitae, justo. Nullam dictum felis eu pede mollis pretium. Integer tincidunt. Cras dapibus. Vivamus elementum semper nisi. Aenean vulputate eleifend tellus. Aenean leo ligula, porttitor eu, consequat vitae, eleifend ac, enim. Aliquam lorem ante, dapibus in, viverra quis, feugiat a, tellus. Phasellus viverra nulla ut metus varius laoreet.</p>
</section>
<span class="btn feature-btn">Book now</span>

<!-- Footer -->
<footer class="abs footer" role="contentinfo">
  <h4 style="left:113px">ABOUT</h4>
  <p class="about">Lorem ipsum dolor sit amet, consectetuer adipiscing elit. Aenean commodo ligula eget dolor. Aenean massa. Cum sociis natoque penatibus et magnis dis parturient montes, nascetur ridiculus mus. Donec quam felis, ultricies nec, pellentesque eu, pretium quis, sem. <span class="green">READ MORE</span></p>
  <h4 style="left:428px">WHAT WE OFFER</h4>
  <ul><li>BIKE RENTAL AND PRICING</li><li>GUIDED TOURS AND PRICING</li><li>RECOMMENDED PACKAGE DEALS</li></ul>
  <h4 style="left:698px">CONTACT</h4>
  <div class="contact">
    <div><svg width="12" height="12" viewBox="0 0 12 12"><path d="M2 1h3l1 3-2 1a7 7 0 0 0 3 3l1-2 3 1v3c-6 1-10-3-9-9z" fill="#3cb521"/></svg><span>0100 200 300</span></div>
    <div><svg width="12" height="12" viewBox="0 0 12 12"><rect x="1" y="3" width="10" height="7" fill="#3cb521"/><path d="m1 3 5 4 5-4" fill="none" stroke="#0e1820"/></svg><span>hello@ridgeline.example</span></div>
    <div><svg width="12" height="12" viewBox="0 0 12 12"><path d="M6 0a4 4 0 0 1 4 4c0 3-4 8-4 8S2 7 2 4a4 4 0 0 1 4-4z" fill="#3cb521"/><circle cx="6" cy="4" r="1.5" fill="#0e1820"/></svg><span>Lorem ipsum dolor sit<br>amet, consecte NZ</span></div>
  </div>
  <h4 style="left:915px">SOCIAL LINKS</h4>
  <div class="abs social"><span></span><span></span><span></span><span></span></div>
  <hr>
  <div class="abs footer-brand">RIDGELINE</div>
  <p class="copy">Copyright © 2018 - RIDGELINE - All rights reserved.</p>
</footer>

</body>
</html>
```